Vital Spark Electrical in need of a business card design

We need a new business card designed for our electrical business. We have a logo already which I will attach below.
Would like the business card to be..
-BLACK background preferably, possibly white back ground behind logo if colours clash.
-White & Blue (logo blue) text
Something that makes the logo pop, & a modern look. Possibly minimal clean format.

REQUIRE:
-Logo on front & back

TEXT TO INCLUDE (ON ONE SIDE):

Tom Harlow
Director/Electrician
M: 0417 365 208
E:info@vitalsparkelectrical-example.com.au
W:www.vitalsparkelectrical-example.com.au
R.E.C 57318

Custom/New Homes
Renovations
Commercial Office/Shop Fit-outs
Communications & Security Cameras
Electric Vehicle Chargers
Airconditioning
Updates

Requirements
Nice to have
• Possibly even lighten the grey shades for the words 'Vital' & 'Spark' to be more easily read on a black background.

```html
<!DOCTYPE html>
<html lang="en">
<head>
<meta charset="utf-8">
<title>Vital Spark Electrical – Business Card</title>
<link rel="stylesheet" href="https://fonts.googleapis.com/css2?family=Mulish:wght@400;500;600;700&display=swap">
<style>
  :root {
    --stage: #c0c0c0;
    --card-dark: #000000;
    --card-glow: #2a2a2a;
    --footer-band: #1a1a1a;
    --blue: #0aa0dd;
    --white: #ffffff;
    --soft-white: #e6e6e6;
    --divider: #2c2c2c;
  }
  * { margin: 0; padding: 0; box-sizing: border-box; }
  html, body {
    width: 1033px; height: 1200px; overflow: hidden;
    background: var(--stage);
    font-family: "Mulish", sans-serif;
    color: var(--white);
  }
  .canvas { position: relative; width: 1033px; height: 1200px; }

  .card {
    position: absolute; left: 122px; width: 790px; height: 451px;
    background: radial-gradient(ellipse at 45% 50%, var(--card-glow) 0%, #121212 40%, var(--card-dark) 80%);
    box-shadow: 0 6px 18px rgba(0,0,0,0.28);
    overflow: hidden;
  }
  .card--front { top: 100px; }
  .card--back { top: 649px; }

  /* brand name */
  .brand { position: absolute; display: flex; align-items: center; }
  .brand__mark { background: var(--blue); flex: none; }
  .brand__name { color: var(--white); font-weight: 600; white-space: nowrap; letter-spacing: 0.2px; }

  .card--front .brand { left: 23px; top: 62px; gap: 14px; }
  .card--front .brand__mark { width: 30px; height: 30px; }
  .card--front .brand__name { font-size: 30px; }

  .card--back .brand { left: 0; right: 0; top: 176px; justify-content: center; gap: 20px; }
  .card--back .brand__mark { width: 46px; height: 46px; }
  .card--back .brand__name { font-size: 46px; }

  /* contact block */
  .person__name {
    position: absolute; left: 35px; top: 160px;
    font-size: 37px; font-weight: 700; letter-spacing: -0.3px;
    text-transform: uppercase;
  }
  .person__role {
    position: absolute; left: 35px; top: 206px;
    font-size: 20px; font-weight: 400; color: var(--soft-white);
  }
  .contact { position: absolute; left: 35px; top: 260px; list-style: none; }
  .contact__item { display: flex; align-items: center; height: 33px; font-size: 16px; font-weight: 500; }
  .contact__icon { width: 17px; height: 17px; margin-right: 14px; fill: var(--blue); }

  .divider {
    position: absolute; left: 423px; top: 78px; width: 1px; height: 251px;
    background: linear-gradient(var(--card-dark), var(--divider) 30%, var(--divider) 70%, var(--card-dark));
  }

  /* services */
  .services { position: absolute; left: 459px; top: 137px; list-style: none; }
  .services__item { display: flex; align-items: center; height: 35.3px; font-size: 16px; font-weight: 500; white-space: nowrap; }
  .services__tick { width: 15px; height: 13px; margin-right: 6px; fill: var(--white); }

  .accent-stripe {
    position: absolute; left: 413px; top: 384px; width: 377px; height: 8px;
    background: var(--blue);
    clip-path: polygon(0 0, 100% 0, 100% 100%, 8px 100%);
  }
  .footer-band {
    position: absolute; left: 0; top: 392px; width: 790px; height: 59px;
    background: var(--footer-band);
    display: flex; align-items: center; justify-content: center;
  }
  .web-line { font-size: 15.5px; font-weight: 400; color: var(--soft-white); white-space: nowrap; }
  .web-line__sep { margin: 0 13px; }

  .card--back .web-line {
    position: absolute; left: 0; right: 0; top: 288px; text-align: center; font-size: 17px;
  }
</style>
</head>
<body>
<div class="canvas">

  <section class="card card--front" aria-label="Business card front">
    <div class="brand">
      <span class="brand__mark"></span>
      <span class="brand__name">Vital Spark Electrical</span>
    </div>

    <h1 class="person__name">Tom Harlow</h1>
    <p class="person__role">Director/Electrician</p>

    <ul class="contact">
      <li class="contact__item">
        <svg class="contact__icon" viewBox="0 0 24 24" aria-hidden="true"><path d="M6.6 10.8a15.1 15.1 0 0 0 6.6 6.6l2.2-2.2c.3-.3.7-.4 1-.2 1.1.4 2.3.6 3.6.6.6 0 1 .4 1 1V20c0 .6-.4 1-1 1A17 17 0 0 1 3 4c0-.6.4-1 1-1h3.5c.6 0 1 .4 1 1 0 1.3.2 2.5.6 3.6.1.3 0 .7-.2 1l-2.3 2.2z"/></svg>
        0417 365 208
      </li>
      <li class="contact__item">
        <svg class="contact__icon" viewBox="0 0 24 24" aria-hidden="true"><path d="M2 5h20v2l-10 6L2 7z"/><path d="M2 9.3l10 6 10-6V19H2z"/></svg>
        info@vitalsparkelectrical-example.com.au
      </li>
    </ul>

    <div class="divider"></div>

    <ul class="services">
      <li class="services__item"><svg class="services__tick" viewBox="0 0 16 13" aria-hidden="true"><path d="M0 7l2.2-2.2L6 8.4 13.8 0.6 16 2.8 6 12.8z"/></svg>Custom/New Homes</li>
      <li class="services__item"><svg class="services__tick" viewBox="0 0 16 13" aria-hidden="true"><path d="M0 7l2.2-2.2L6 8.4 13.8 0.6 16 2.8 6 12.8z"/></svg>Renovations</li>
      <li class="services__item"><svg class="services__tick" viewBox="0 0 16 13" aria-hidden="true"><path d="M0 7l2.2-2.2L6 8.4 13.8 0.6 16 2.8 6 12.8z"/></svg>Commercial Office/Shop Fit-outs</li>
      <li class="services__item"><svg class="services__tick" viewBox="0 0 16 13" aria-hidden="true"><path d="M0 7l2.2-2.2L6 8.4 13.8 0.6 16 2.8 6 12.8z"/></svg>Communications &amp; Security Cameras</li>
      <li class="services__item"><svg class="services__tick" viewBox="0 0 16 13" aria-hidden="true"><path d="M0 7l2.2-2.2L6 8.4 13.8 0.6 16 2.8 6 12.8z"/></svg>Electric Vehicle Chargers</li>
      <li class="services__item"><svg class="services__tick" viewBox="0 0 16 13" aria-hidden="true"><path d="M0 7l2.2-2.2L6 8.4 13.8 0.6 16 2.8 6 12.8z"/></svg>Airconditioning</li>
    </ul>

    <div class="accent-stripe"></div>
    <footer class="footer-band">
      <p class="web-line">www.vitalsparkelectrical-example.com.au<span class="web-line__sep">|</span>R.E.C 57318</p>
    </footer>
  </section>

  <section class="card card--back" aria-label="Business card back">
    <div class="brand">
      <span class="brand__mark"></span>
      <span class="brand__name">Vital Spark Electrical</span>
    </div>
    <p class="web-line">www.vitalsparkelectrical-example.com.au<span class="web-line__sep">|</span>R.E.C 57318</p>
  </section>

</div>
</body>
</html>
```